General Contractor Company introduction and presentation

i need a company presentation design for a construction company called R9 Builders Corp. we build brand ground up affordable apartment building as well Remodeling of apartment units and commercial buildings.
company was established in June 2020.

```html
<!DOCTYPE html>
<html lang="en">
<head>
<meta charset="utf-8">
<title>R9 Builders Corp. – Company Presentation</title>
<link href="https://fonts.googleapis.com/css2?family=Montserrat:ital,wght@0,400;0,500;0,600;0,700;0,800;1,400;1,500&display=swap" rel="stylesheet">
<style>
:root{
  --green:#7ad84e;
  --green-dark:#5cbf33;
  --ink:#333;
  --grey:#666;
  --grey-mid:#6b6b6b;
  --grey-light:#e4e4e4;
  --muted:#8a8a8a;
  --board:#d9d9d9;
  --photo-a:#8a8a8a;
  --photo-b:#4c4c4c;
}
*{margin:0;padding:0;box-sizing:border-box}
html,body{width:1041px;height:1200px;overflow:hidden}
body{background:var(--board);font-family:'Montserrat',sans-serif;color:var(--ink);position:relative}
.slide{position:absolute;width:537px;height:302px;background:#fff;transform:scale(.5812);transform-origin:0 0;box-shadow:0 4px 10px rgba(0,0,0,.28);overflow:hidden}
.c1{left:36px}.c2{left:365px}.c3{left:693px}
.r1{top:32px}.r2{top:223px}.r3{top:415px}.r4{top:606px}.r5{top:800px}.r6{top:992px}
.abs{position:absolute}
.photo{position:absolute;background:linear-gradient(160deg,var(--photo-a),var(--photo-b))}
.map{position:absolute;background:radial-gradient(ellipse at center,#efefef 0%,#f7f7f7 55%,#fff 75%)}
.brand-tag{position:absolute;top:12px;right:12px;display:flex;align-items:center;gap:3px;font-size:5px;font-weight:700;color:var(--grey-mid);letter-spacing:.3px}
.brand-tag i{display:block;width:9px;height:9px;background:var(--green)}
.title{position:absolute;left:20px;top:14px;font-size:17px;font-weight:600;color:var(--ink)}
.rule{position:absolute;left:20px;top:40px;display:flex;gap:2px;align-items:center}
.rule b{display:block;width:14px;height:2.5px;background:var(--green)}
.rule i{display:block;width:2.5px;height:2.5px;background:var(--grey-mid)}
.footer{position:absolute;left:22px;right:22px;bottom:12px;display:flex;align-items:center;gap:4px;font-size:5px;color:var(--grey);letter-spacing:.3px}
.footer span.line{flex:1;height:.6px;background:#999}
.fine{font-size:4.6px;line-height:1.4;color:var(--muted)}
.small{font-size:6px;line-height:1.4;color:var(--muted)}
.green{color:var(--green)}
.white{color:#fff}
.h-item{font-size:8px;font-weight:600;color:var(--ink)}
.icon-circle{position:absolute;border-radius:50%;background:var(--green);display:flex;align-items:center;justify-content:center}
.icon-sq{position:absolute;display:flex;align-items:center;justify-content:center}
</style>
</head>
<body>

<!-- 1 Cover -->
<section class="slide c1 r1" style="background:#555">
  <div class="photo" style="inset:0" role="img" aria-label="Construction site skyline with cranes, greyscale"></div>
  <div class="abs" style="left:0;right:0;top:95px;text-align:center;color:#fff">
    <div style="display:inline-flex;align-items:center;gap:6px;font-size:15px;font-weight:700;letter-spacing:2px"><i style="display:block;width:14px;height:14px;background:var(--green)"></i>R9 BUILDERS CORP.</div>
  </div>
  <div class="abs" style="left:0;right:0;top:198px;text-align:center;font-size:25px;font-weight:700;color:var(--green)">BUSINESS MARKETING</div>
  <div class="abs white" style="left:0;right:0;top:233px;text-align:center;font-size:7px;font-style:italic;line-height:1.3">Lorem ipsum dolor sit amet, consectetuer adipiscing elit,<br>sed diam nonum</div>
  <div class="abs" style="left:0;right:0;top:252px;height:2px;background:var(--green)"></div>
</section>

<!-- 2 Agenda -->
<section class="slide c2 r1">
  <div class="brand-tag"><i></i>R9 BUILDERS</div>
  <div class="photo" style="left:60px;top:63px;width:175px;height:175px" role="img" aria-label="Engineers reviewing plans on site"></div>
  <div class="abs white" style="left:83px;top:128px;font-size:28px;font-weight:700">Agenda</div>
  <div class="abs" style="left:52px;top:208px;width:37px;height:37px;background:var(--green)"></div>
  <div class="abs" style="left:265px;top:65px;width:220px">
    <div style="height:50px"><div class="green" style="font-size:10px;font-weight:500">1. Lorem ipsum</div><div class="fine" style="margin-top:3px;padding-left:12px">Lorem ipsum dolor sit amet, consectetuer adipiscing elit, sed diam nonummy nibh euismod tincid</div></div>
    <div style="height:50px"><div class="green" style="font-size:10px;font-weight:500">2. Lorem ipsum</div><div class="fine" style="margin-top:3px;padding-left:12px">Lorem ipsum dolor sit amet, consectetuer adipiscing elit, sed diam nonummy nibh euismod tincid</div></div>
    <div style="height:47px"><div class="green" style="font-size:10px;font-weight:500">3. Lorem ipsum</div><div class="fine" style="margin-top:3px;padding-left:12px">Lorem ipsum dolor sit amet, consectetuer adipiscing elit, sed diam nonummy nibh euismod tincid</div></div>
    <div><div class="green" style="font-size:10px;font-weight:500">4. Lorem ipsum</div><div class="fine" style="margin-top:3px;padding-left:12px">Lorem ipsum dolor sit amet, consectetuer adipiscing elit, sed diam nonummy nibh euismod tincid</div></div>
  </div>
  <div class="footer">www.r9builders.com<span class="line"></span>2</div>
</section>

<!-- 3 Services overview -->
<section class="slide c3 r1">
  <div class="brand-tag"><i></i>R9 BUILDERS</div>
  <div class="title">Text Added Hare</div>
  <div class="abs" style="left:60px;top:76px;width:190px">
    <div style="height:47px"><div style="font-size:6.5px;font-weight:600">01. Aliquam Erat Volutpat</div><div class="fine" style="padding-left:12px">Lorem ipsum dolor sit amet, consectetuer adipiscing elit, sed diam nonummy nibh euismod</div></div>
    <div style="height:50px"><div style="font-size:6.5px;font-weight:600">02. Consectetuer Adipiscing Elit</div><div class="fine" style="padding-left:12px">Lorem ipsum dolor sit amet, consectetuer adipiscing elit, sed diam nonummy nibh euismod tincidunt ut laoreet</div></div>
    <div style="height:46px"><div style="font-size:6.5px;font-weight:600">03. Duis Autem Vel Eum</div><div class="fine" style="padding-left:12px">Lorem ipsum dolor sit amet, consectetuer adipiscing elit, sed diam nonummy nibh euismod tincidunt.</div></div>
    <div><div style="font-size:6.5px;font-weight:600">04. Aliquam Erat Volutpat</div><div class="fine" style="padding-left:12px">Lorem ipsum dolor sit amet, consectetuer adipiscing elit, sed diam nonummy nibh euismod tincidunt ut laoreet.</div></div>
  </div>
  <div class="abs" style="left:294px;top:70px;width:156px;height:187px;background:var(--grey-mid)"></div>
  <div class="abs white" style="left:326px;top:88px;width:118px">
    <div style="height:57px"><div style="font-size:9px;font-weight:600">Lorem Ipsum</div><div style="font-size:4.6px;line-height:1.35">ipsum dolor sit amet, cons ectetuer adipiscing elit, sed diam nonummy</div></div>
    <div style="height:58px"><div style="font-size:9px;font-weight:600">Lorem Ipsum</div><div style="font-size:4.6px;line-height:1.35">ipsum dolor sit amet, cons ectetuer adipiscing elit, sed diam nonummy nibh euismod tincidunt ut laoreet</div></div>
    <div><div style="font-size:9px;font-weight:600">Lorem Ipsum</div><div style="font-size:4.6px;line-height:1.35">ipsum dolor sit amet, cons ectetuer adipiscing elit, sed diam nonummy</div></div>
  </div>
  <div class="icon-circle" style="left:252px;top:88px;width:40px;height:40px;border:3px solid #fff"><svg width="16" height="16" viewBox="0 0 16 16" fill="none" stroke="#fff" stroke-width="1.3"><rect x="2" y="3" width="12" height="8"/><path d="M5 14h6M8 11v3M4 9l3-3 2 2 3-3"/></svg></div>
  <div class="icon-circle" style="left:252px;top:143px;width:40px;height:40px;border:3px solid #fff"><svg width="16" height="16" viewBox="0 0 16 16" fill="none" stroke="#fff" stroke-width="1.3"><path d="M4 10a3 3 0 0 1 1-6 4 4 0 0 1 7 1 2.5 2.5 0 0 1 0 5z"/><path d="M8 10v5M6 13l2 2 2-2"/></svg></div>
  <div class="icon-circle" style="left:252px;top:202px;width:40px;height:40px;border:3px solid #fff"><svg width="16" height="16" viewBox="0 0 16 16" fill="#fff" stroke="#fff" stroke-width="1.2"><path d="M3 12l4-5 3 3 3-6" fill="none"/><circle cx="3" cy="12" r="1.5"/><circle cx="7" cy="7" r="1.5"/><circle cx="10" cy="10" r="1.5"/><circle cx="13" cy="4" r="1.5"/></svg></div>
  <div class="footer">www.r9builders.com<span class="line"></span>3</div>
</section>

<!-- 4 About -->
<section class="slide c1 r2">
  <div class="brand-tag"><i></i>R9 BUILDERS</div>
  <div class="abs" style="left:23px;top:22px;font-size:17px;font-weight:600;line-height:1.3">Lorem Ipsum<br>Dolor Sit<br>Ametkeeper.</div>
  <div class="rule" style="left:23px;top:100px"><b></b><i></i><i></i></div>
  <div class="abs small" style="left:23px;top:118px;width:153px;font-size:5px;text-align:justify">
    <p>Lorem ipsum dolor sit amet, consectetuer adipiscing elit, sed diam nonummy nibh euismod tincidunt ut laoreet dolore magna aliquam erat volutpat.</p>
    <p style="margin-top:7px">Ut wisi enim ad minim veniam, quis nostrud exerci tation ullamcorper suscipit lobortis nisl ut aliquip ex ea commodo consequat. Duis autem vel eum iriure dolor in hendrerit in vulputate velit esse molestie consequat,</p>
    <p style="margin-top:7px">vel illum dolore eu feugiat nulla facilisis at vero eros et accumsan et iusto odio dignissim qui blandit praesent luptatum zzril delenit augue duis dolore te feugait nulla facilisi.</p>
  </div>
  <div class="photo" style="left:210px;top:51px;width:327px;height:131px" role="img" aria-label="Site engineer in hard hat reviewing building frame"></div>
  <div class="abs small" style="left:210px;top:196px;width:285px;font-size:5px">
    <p>Lorem ipsum dolor sit amet, consectetuer adipiscing elit, sed diam nonummy nibh euismod tincidunt erat volutpat.</p>
    <p style="margin-top:6px">Ut wisi enim ad minim veniam, quis nostrud exerci tation suscipit lobortis nisl ut aliquip ex ea commodo consequat. Ut wisi enim ad minim veniam, quis nostrud exerci tation ullamcorper suscipit lobortis nisl ut aliquip ex ea commodo consequat.</p>
  </div>
  <div class="footer">www.r9builders.com<span class="line"></span>4</div>
</section>

<!-- 5 Process -->
<section class="slide c2 r2">
  <div class="brand-tag"><i></i>R9 BUILDERS</div>
  <div class="title">Text Added Hare</div>
  <div class="rule"><b></b><i></i><i></i></div>
  <div class="map" style="left:60px;top:50px;width:420px;height:175px" role="img" aria-label="Faint world map background"></div>
  <svg class="abs" style="left:0;top:0" width="537" height="302" viewBox="0 0 537 302" fill="none" stroke="#5f5f5f" stroke-width="3">
    <path d="M104 73h80a8 8 0 0 1 8 8v23M192 104v20l-28 55v23a8 8 0 0 1-8 8H105a8 8 0 0 1-8-8V81a8 8 0 0 1 8-8"/>
    <path d="M228 73h80a8 8 0 0 1 8 8v23M316 104v20l-28 55v23a8 8 0 0 1-8 8h-52a8 8 0 0 1-8-8v-20"/>
    <path d="M220 180l28-55V81a8 8 0 0 1 8-8"/>
    <path d="M352 73h78a8 8 0 0 1 8 8v121a8 8 0 0 1-8 8h-78a8 8 0 0 1-8-8v-20M344 182l28-57"/>
    <circle cx="192" cy="104" r="3.5" fill="#5f5f5f"/><circle cx="220" cy="180" r="3.5" fill="#5f5f5f"/><circle cx="316" cy="104" r="3.5" fill="#5f5f5f"/><circle cx="344" cy="182" r="3.5" fill="#5f5f5f"/>
  </svg>
  <svg class="abs" style="left:137px;top:86px" width="12" height="14" viewBox="0 0 12 14" fill="none" stroke="var(--green)" stroke-width="1.2"><path d="M6 1a4 4 0 0 0-2 7.5V11h4V8.5A4 4 0 0 0 6 1zM4 13h4"/></svg>
  <svg class="abs" style="left:260px;top:88px" width="14" height="10" viewBox="0 0 14 10" fill="none" stroke="var(--green)" stroke-width="1.2"><rect x="1" y="1" width="12" height="8"/><path d="M1 1l6 5 6-5"/></svg>
  <svg class="abs" style="left:384px;top:86px" width="12" height="12" viewBox="0 0 12 12" fill="none" stroke="var(--green)" stroke-width="1.2"><path d="M1 1v10h10M3 8l3-3 2 2 3-4"/></svg>
  <div class="abs" style="left:104px;top:103px;width:80px;text-align:center"><div style="font-size:7px;font-weight:600">IDEA</div><div class="fine" style="font-size:4px;margin-top:4px;color:#777">Lorem ipsum dolor sit amet, consectetuer adipiscing elit, sed diam nonummy nibh euismod tincidunt ut laoreet dolore magna aliquam erat volutpat. Ut wisi enim ad minim veniam, quis nostrud exerci tation ullamcorper suscipit lobortis nisl ut aliquip ex ea</div></div>
  <div class="abs" style="left:228px;top:103px;width:80px;text-align:center"><div style="font-size:7px;font-weight:600">PROMOTION</div><div class="fine" style="font-size:4px;margin-top:4px;color:#777">Lorem ipsum dolor sit amet, consectetuer adipiscing elit, sed diam nonummy nibh euismod tincidunt ut laoreet dolore magna aliquam erat volutpat. Ut wisi enim ad minim veniam, quis nostrud exerci tation ullamcorper suscipit lobortis nisl ut aliquip ex ea</div></div>
  <div class="abs" style="left:352px;top:103px;width:80px;text-align:center"><div style="font-size:7px;font-weight:600">GROWTH</div><div class="fine" style="font-size:4px;margin-top:4px;color:#777">Lorem ipsum dolor sit amet, consectetuer adipiscing elit, sed diam nonummy nibh euismod tincidunt ut laoreet dolore magna aliquam erat volutpat. Ut wisi enim ad minim veniam, quis nostrud exerci tation ullamcorper suscipit lobortis nisl ut aliquip ex ea</div></div>
  <div class="abs fine" style="left:62px;top:228px;width:413px;text-align:center;color:#666">Lorem ipsum dolor sit amet, consectetuer adipiscing elit, sed diam nonummy nibh euismod tincidunt ut laoreet dolore magna aliquam erat volutpat. Ut wisi enim ad minim veniam, quis nostrud exerci tation ullamcorper suscipit lobortis nisl ut aliquip ex ea commodo consequat. Duis autem vel eum iriure dolor in hendrerit i</div>
  <div class="footer">www.r9builders.com<span class="line"></span>5</div>
</section>

<!-- 6 Numbered text -->
<section class="slide c3 r2">
  <div class="brand-tag"><i></i>R9 BUILDERS</div>
  <div class="title">Text Added Hare</div>
  <div class="rule"><b></b><i></i><i></i></div>
  <div class="abs" style="left:35px;top:62px;width:470px">
    <div style="height:68px"><div class="h-item"><span class="green">1.</span> Text Added Here</div><div class="fine" style="margin-top:3px;color:#888">Lorem ipsum dolor sit amet, cons ectetuer adipiscing elit, sed diam nonummy nibh euismod tincidunt ut laoreet dolore magna aliquam erat volutpat. Ut wisi enim ad minim veniam, quis nostrud exerci tation ullamcorper suscipit lobortis nisl ut aliquip ex ea commodo consequat. Lorem ipsum dolor sit amet, cons ectetuer adipiscing elit, sed diam nonummy nibh euismod tincidunt ut laoreet dolore magna aliquam erat volutpat. Ut wisi enim ad minim veniam, quis nostrud exerci tation ullamcorper suscipit lobortis nisl ut aliquip ex ea commodo consequat.</div></div>
    <div style="height:75px"><div class="h-item"><span class="green">2.</span> Text Added Here</div><div class="fine" style="margin-top:3px;color:#888">Lorem ipsum dolor sit amet, cons ectetuer adipiscing elit, sed diam nonummy nibh euismod tincidunt ut laoreet dolore magna aliquam erat volutpat. Ut wisi enim ad minim veniam, quis nostrud exerci tation ullamcorper suscipit lobortis nisl ut aliquip ex ea commodo consequat. Lorem ipsum dolor sit amet, cons ectetuer adipiscing elit, sed diam nonummy nibh euismod tincidunt ut laoreet dolore magna aliquam erat volutpat. Ut wisi enim ad minim veniam, quis nostrud exerci tation ullamcorper suscipit lobortis nisl ut aliquip ex ea commodo consequat.</div></div>
    <div><div class="h-item"><span class="green">3.</span> Text Added Here</div><div class="fine" style="margin-top:3px;color:#888">Lorem ipsum dolor sit amet, cons ectetuer adipiscing elit, sed diam nonummy nibh euismod tincidunt ut laoreet dolore magna aliquam erat volutpat. Ut wisi enim ad minim veniam, quis nostrud exerci tation ullamcorper suscipit lobortis nisl ut aliquip ex ea commodo consequat. Lorem ipsum dolor sit amet, cons ectetuer adipiscing elit, sed diam nonummy nibh euismod tincidunt ut laoreet dolore magna aliquam erat volutpat. Ut wisi enim ad minim veniam, quis nostrud exerci tation ullamcorper suscipit lobortis nisl ut aliquip ex ea commodo consequat.</div></div>
  </div>
  <div class="footer">www.r9builders.com<span class="line"></span>6</div>
</section>

<!-- 7 Subject -->
<section class="slide c1 r3">
  <div class="brand-tag"><i></i>R9 BUILDERS</div>
  <div class="abs" style="left:0;top:0;width:155px;height:20px;background:var(--green)"></div>
  <div class="photo" style="left:155px;top:0;width:101px;height:187px" role="img" aria-label="Engineer holding drawings at a site"></div>
  <div class="abs" style="left:27px;top:48px;font-size:17px;font-weight:600;line-height:1.35">Subject<br>Title</div>
  <div class="rule" style="left:27px;top:102px"><b></b><i></i><i></i></div>
  <div class="abs" style="left:27px;top:115px;width:118px;font-size:6px;line-height:1.55;color:#888;font-weight:500">Lorem ipsum dolor sit amet, consectetuer adipiscing elit, sed diam nonummy nibh euismod tincidunt ut laoreet dolore magna aliquam erat volutpat. Ut wisi enim ad minim veniam, quis nostrud exerci tation ullamcorper suscipit lobortis nisl ut aliquip ex ea commodo consequat. Duis autem vel eum iriure.</div>
  <div class="abs" style="left:226px;top:77px;width:311px;height:162px;background:var(--green)"></div>
  <div class="photo" style="left:272px;top:95px;width:107px;height:173px" role="img" aria-label="Modern apartment building facade"></div>
  <div class="abs" style="left:397px;top:98px;font-size:12px;font-weight:600;line-height:1.25;color:#3a3a3a">Lorem Ipsum<br>Dolor Sit<br>Ametkeeper.</div>
  <div class="abs white" style="left:397px;top:160px;width:120px;font-size:5.5px;line-height:1.35">Lorem ipsum dolor sit amet, consectetuer adipiscing<br><br>elit, sed diam nonummy nibh euismod tincidunt ut laoreet dolore magna</div>
  <div class="footer">www.r9builders.com<span class="line"></span>7</div>
</section>

<!-- 8 Section break -->
<section class="slide c2 r3">
  <div class="photo" style="left:25px;top:21px;width:487px;height:260px" role="img" aria-label="Construction site with cranes, darkened greyscale"></div>
  <div class="abs white" style="left:240px;top:108px;font-size:14px">Section</div>
  <div class="abs green" style="left:240px;top:122px;font-size:28px;font-weight:800">Break</div>
  <div class="abs white" style="left:240px;top:165px;width:200px;font-size:8px;line-height:1.3">Lorem ipsum dolor sit amet, consectetuer sed diam nonummy euismod tincid</div>
</section>

<!-- 9 Projects -->
<section class="slide c3 r3">
  <div class="brand-tag"><i></i>R9 BUILDERS</div>
  <div class="title">Text Added Hare</div>
  <div class="rule"><b></b><i></i><i></i></div>
  <div class="photo" style="left:43px;top:63px;width:162px;height:193px" role="img" aria-label="Worker tying rebar on site"></div>
  <div class="icon-circle" style="left:232px;top:72px;width:40px;height:40px"><svg width="18" height="18" viewBox="0 0 18 18" fill="none" stroke="#fff" stroke-width="1.3"><circle cx="9" cy="9" r="7"/><circle cx="9" cy="9" r="4"/><circle cx="9" cy="9" r="1"/></svg></div>
  <div class="icon-circle" style="left:232px;top:138px;width:40px;height:40px"><svg width="18" height="18" viewBox="0 0 18 18" fill="none" stroke="#fff" stroke-width="1.3"><circle cx="9" cy="9" r="7"/><circle cx="9" cy="9" r="4"/><circle cx="9" cy="9" r="1"/></svg></div>
  <div class="icon-circle" style="left:232px;top:208px;width:40px;height:40px"><svg width="18" height="18" viewBox="0 0 18 18" fill="none" stroke="#fff" stroke-width="1.3"><circle cx="9" cy="9" r="7"/><circle cx="9" cy="9" r="4"/><circle cx="9" cy="9" r="1"/></svg></div>
  <div class="abs" style="left:287px;top:72px;width:180px"><div style="font-size:8px;font-weight:600">Project name</div><div class="fine">Lorem ipsum dolor sit amet. nec an dictas equidem appellantur, ut has commune accommodare. Mea illum, iudus solet idpro.</div></div>
  <div class="abs" style="left:287px;top:138px;width:180px"><div style="font-size:8px;font-weight:600">Project name</div><div class="fine">Lorem ipsum dolor sit amet. nec an dictas equidem appellantur, ut has commune accommodare. Mea illum, iudus solet idpro.</div></div>
  <div class="abs" style="left:287px;top:208px;width:180px"><div style="font-size:8px;font-weight:600">Project name</div><div class="fine">Lorem ipsum dolor sit amet. nec an dictas equidem appellantur, ut has commune accommodare. Mea illum, iudus solet idpro.</div></div>
  <div class="footer">www.r9builders.com<span class="line"></span>9</div>
</section>

<!-- 10 Market chart -->
<section class="slide c1 r4">
  <div class="brand-tag"><i></i>R9 BUILDERS</div>
  <div class="abs" style="left:28px;top:20px;font-size:14px;font-weight:600;line-height:1.3">Market<br>Opportunities.</div>
  <div class="rule" style="left:28px;top:76px"><b></b><i></i><i></i></div>
  <div class="abs" style="left:0;top:95px;width:185px;height:150px;background:var(--grey-light)"></div>
  <div class="abs" style="left:24px;top:107px;width:140px;font-size:6.3px;line-height:1.33;color:#8a8a8a">Lorem ipsum dolor sit amet, consectetuer adipiscing elit, sed diam nonummy nibh euismod tincidunt ut laoreet dolore magna aliquam erat volutpat. Ut wisi enim ad minim veniam, quis nostrud exerci tation ullamcorper suscipit lobortis nisl ut aliquip ex ea commodo consequat. Duis autem vel eum iriure dolor in hendrerit i</div>
  <div class="abs" style="left:222px;top:32px;font-size:7px;font-weight:500;color:#555">CONSECTETUER ADIPISCING</div>
  <svg class="abs" style="left:210px;top:50px" width="300" height="150" viewBox="0 0 300 150" font-family="Montserrat, sans-serif" font-size="7" fill="#444">
    <g stroke="#cfcfcf" stroke-width=".6"><line x1="24" y1="8" x2="287" y2="8"/><line x1="24" y1="28.7" x2="287" y2="28.7"/><line x1="24" y1="49.3" x2="287" y2="49.3"/><line x1="24" y1="70" x2="287" y2="70"/><line x1="24" y1="90.7" x2="287" y2="90.7"/><line x1="24" y1="111.3" x2="287" y2="111.3"/><line x1="24" y1="132" x2="287" y2="132" stroke="#888"/><line x1="24" y1="8" x2="24" y2="132" stroke="#888"/><line x1="287" y1="8" x2="287" y2="132"/></g>
    <g text-anchor="end"><text x="18" y="10">60</text><text x="18" y="31">50</text><text x="18" y="52">40</text><text x="18" y="72">30</text><text x="18" y="93">20</text><text x="18" y="114">10</text><text x="18" y="134">0</text></g>
    <rect x="47" y="22" width="30" height="110" fill="var(--green)"/>
    <rect x="104" y="64" width="30" height="68" fill="var(--grey-mid)"/>
    <rect x="161" y="35" width="30" height="97" fill="var(--green)"/>
    <rect x="219" y="74" width="30" height="58" fill="var(--grey-mid)"/>
    <g text-anchor="middle"><text x="62" y="147">JAN</text><text x="119" y="147">FEB</text><text x="176" y="147">MAR</text><text x="234" y="147">APR</text></g>
  </svg>
  <div class="abs" style="left:218px;top:217px;width:130px"><div style="font-size:7.5px;font-weight:500"><span style="display:inline-block;width:6px;height:6px;border-radius:50%;background:var(--green);margin-right:4px"></span>Lorem Ipsum</div><div class="fine" style="padding-left:10px">Lorem ipsum dolor sit amet, consectetuer adipiscing elit, sed diam nonummy nibh euismod tincidunt ut laoreet</div></div>
  <div class="abs" style="left:355px;top:217px;width:130px"><div style="font-size:7.5px;font-weight:500"><span style="display:inline-block;width:6px;height:6px;border-radius:50%;background:var(--green);margin-right:4px"></span>Lorem Ipsum</div><div class="fine" style="padding-left:10px">Lorem ipsum dolor sit amet, consectetuer adipiscing elit, sed diam nonummy nibh euismod tincidunt ut laoreet</div></div>
  <div class="footer">www.r9builders.com<span class="line"></span>10</div>
</section>

<!-- 11 Four cards -->
<section class="slide c2 r4">
  <div class="brand-tag"><i></i>R9 BUILDERS</div>
  <div class="title">Text Added Hare</div>
  <div class="rule"><b></b><i></i><i></i></div>
  <div class="map" style="left:60px;top:55px;width:420px;height:190px" role="img" aria-label="Faint world map background"></div>
  <div class="abs" style="left:70px;top:88px;width:86px;height:120px;border:1.5px solid #555;background:#fff"></div>
  <div class="abs" style="left:171px;top:88px;width:86px;height:120px;border:1.5px solid #555;background:#fff"></div>
  <div class="abs" style="left:272px;top:88px;width:86px;height:120px;border:1.5px solid #555;background:#fff"></div>
  <div class="abs" style="left:372px;top:88px;width:87px;height:120px;border:1.5px solid #555;background:#fff"></div>
  <div class="icon-circle" style="left:96px;top:71px;width:34px;height:34px;border:3px solid #fff"><svg width="14" height="14" viewBox="0 0 14 14" fill="none" stroke="#fff" stroke-width="1.2"><rect x="1" y="2" width="12" height="9"/><path d="M3 5h4M3 8h3M9 5v4"/></svg></div>
  <div class="icon-circle" style="left:197px;top:71px;width:34px;height:34px;border:3px solid #fff"><svg width="14" height="14" viewBox="0 0 14 14" fill="none" stroke="#fff" stroke-width="1.2"><rect x="1" y="2" width="12" height="8"/><path d="M5 13h4M3 8l3-3 2 2 3-3"/></svg></div>
  <div class="icon-circle" style="left:298px;top:71px;width:34px;height:34px;border:3px solid #fff"><svg width="14" height="14" viewBox="0 0 14 14" fill="#fff"><path d="M7 2l6 3-6 3-6-3z"/><path d="M3 7v3c2 2 6 2 8 0V7L7 9z"/></svg></div>
  <div class="icon-circle" style="left:398px;top:71px;width:34px;height:34px;border:3px solid #fff"><svg width="14" height="14" viewBox="0 0 14 14" fill="none" stroke="#fff" stroke-width="1.2"><rect x="1" y="2" width="12" height="10"/><path d="M3 9l3-3 2 2 3-3"/></svg></div>
  <div class="abs" style="left:78px;top:110px;width:72px"><div style="font-size:7px;font-weight:600">Lorem ipsum</div><div class="fine" style="font-size:4px">Ipsum dolor sit amet, cons ectetuer adipiscing elit, sed diam nonummy nibh euismod tincidunt ut laoreet<br><br>ipsum dolor sit amet, cons ectetuer adipiscing elit, sed diam nonummy nibh euismod tincidunt ut laoreet ipsum dolor sit amet, cons ectetuer</div></div>
  <div class="abs" style="left:179px;top:110px;width:72px"><div style="font-size:7px;font-weight:600">Lorem ipsum</div><div class="fine" style="font-size:4px">Ipsum dolor sit amet, cons ectetuer adipiscing elit, sed diam nonummy nibh euismod tincidunt ut laoreet<br><br>ipsum dolor sit amet, cons ectetuer adipiscing elit, sed diam nonummy nibh euismod tincidunt ut laoreet ipsum dolor sit amet, cons ectetuer</div></div>
  <div class="abs" style="left:280px;top:110px;width:72px"><div style="font-size:7px;font-weight:600">Lorem ipsum</div><div class="fine" style="font-size:4px">Ipsum dolor sit amet, cons ectetuer adipiscing elit, sed diam nonummy nibh euismod tincidunt ut laoreet<br><br>ipsum dolor sit amet, cons ectetuer adipiscing elit, sed diam nonummy nibh euismod tincidunt ut laoreet ipsum dolor sit amet, cons ectetuer</div></div>
  <div class="abs" style="left:380px;top:110px;width:72px"><div style="font-size:7px;font-weight:600">Lorem ipsum</div><div class="fine" style="font-size:4px">Ipsum dolor sit amet, cons ectetuer adipiscing elit, sed diam nonummy nibh euismod tincidunt ut laoreet<br><br>ipsum dolor sit amet, cons ectetuer adipiscing elit, sed diam nonummy nibh euismod tincidunt ut laoreet ipsum dolor sit amet, cons ectetuer</div></div>
  <div class="abs" style="left:72px;top:224px;font-size:12px;font-weight:600">+ 35k</div>
  <div class="abs fine" style="left:72px;top:244px;width:300px;font-size:4px;color:#666">Lorem ipsum dolor sit amet, consectetuer adipiscing elit, sed diam nonummy nibh euismod tincidunt ut laoreet dolore magna aliquam erat volutpat. Ut wisi enim ad minim veniam, quis nostrud exerci tation ullamcorper</div>
  <div class="footer">www.r9builders.com<span class="line"></span>11</div>
</section>

<!-- 12 Values -->
<section class="slide c3 r4">
  <div class="brand-tag"><i></i>R9 BUILDERS</div>
  <div class="abs" style="left:32px;top:38px;font-size:17px;font-weight:600;line-height:1.3">Lorem Ipsum<br><span class="green">Dolor Sit</span><br>Ametkeeper.</div>
  <div class="rule" style="left:32px;top:116px"><b></b><i></i><i></i></div>
  <div class="abs" style="left:0;top:155px;width:210px;height:85px;background:var(--grey-light)"></div>
  <div class="abs" style="left:32px;top:165px;width:165px;font-size:6px;line-height:1.3;color:#888">Lorem ipsum dolor sit amet, consectetuer adipiscing elit, sed diam nonummy nibh euismod tincidunt erat volutpat.<br><br>Ut wisi enim ad minim veniam, quis nostrud exerci tation ullamcorper</div>
  <div class="icon-sq" style="left:241px;top:48px;width:40px;height:40px;background:var(--green)"><svg width="20" height="16" viewBox="0 0 20 16" fill="#fff"><circle cx="10" cy="4" r="3"/><circle cx="4" cy="6" r="2"/><circle cx="16" cy="6" r="2"/><path d="M5 15a5 5 0 0 1 10 0zM0 15a4 4 0 0 1 5-4v4zM20 15a4 4 0 0 0-5-4v4z"/></svg></div>
  <div class="icon-sq" style="left:241px;top:125px;width:40px;height:40px;background:var(--green)"><svg width="18" height="18" viewBox="0 0 18 18" fill="#fff"><circle cx="6" cy="3" r="2"/><circle cx="12" cy="3" r="2"/><path d="M3 6h6v6H8v5H4v-5H3zM9 6h6v6h-1v5h-4v-5H9z"/></svg></div>
  <div class="icon-sq" style="left:241px;top:206px;width:40px;height:40px;background:var(--green)"><svg width="20" height="18" viewBox="0 0 20 18" fill="#fff"><path d="M10 10C6 7 5 5 7 3s3 0 3 1c0-1 1-3 3-1s1 4-3 7z"/><path d="M1 12h4l4 2h5l3-2 2 1-5 4H7l-6-2z"/></svg></div>
  <div class="abs" style="left:299px;top:52px;width:210px"><div style="font-size:8.5px;font-weight:700">We Before Me</div><div class="fine">ipsum dolor sit amet, cons ectetuer adipiscing elit, sed diam nonummy nibh euismod tincidunt ut laoreet</div></div>
  <div class="abs" style="left:299px;top:129px;width:210px"><div style="font-size:8.5px;font-weight:700">We Are Good People</div><div class="fine">ipsum dolor sit amet, cons ectetuer adipiscing elit, sed diam nonummy nibh euismod tincidunt ut laoreet dolore magna aliquam erat volutpat.</div></div>
  <div class="abs" style="left:299px;top:210px;width:210px"><div style="font-size:8.5px;font-weight:700">We Work with Heart</div><div class="fine">ipsum dolor sit amet, cons ectetuer adipiscing elit, sed diam nonummy nibh euismod tincidunt</div></div>
  <div class="footer">www.r9builders.com<span class="line"></span>12</div>
</section>

<!-- 13 Timeline -->
<section class="slide c1 r5">
  <div class="brand-tag"><i></i>R9 BUILDERS</div>
  <div class="title">Text Added Hare</div>
  <div class="rule"><b></b><i></i><i></i></div>
  <svg class="abs" style="left:0;top:0" width="537" height="302" viewBox="0 0 537 302" fill="none" stroke="#555" stroke-width="2.2" font-family="Montserrat, sans-serif">
    <line x1="55" y1="171" x2="482" y2="171" stroke-width="1"/>
    <path d="M72 171v-58a14 14 0 0 1 14-14h50a14 14 0 0 1 14 14v58"/>
    <path d="M222 171v-58a14 14 0 0 1 14-14h48a14 14 0 0 1 14 14v58"/>
    <path d="M372 171v-58a14 14 0 0 1 14-14h48a14 14 0 0 1 14 14v58"/>
    <path d="M147 171v45a14 14 0 0 0 14 14h48a14 14 0 0 0 14-14v-45"/>
    <path d="M297 171v45a14 14 0 0 0 14 14h48a14 14 0 0 0 14-14v-45"/>
    <g stroke="#fff" stroke-width="3"><circle cx="110" cy="108" r="11" fill="var(--green)"/><circle cx="260" cy="108" r="11" fill="var(--green)"/><circle cx="410" cy="108" r="11" fill="var(--green)"/><circle cx="185" cy="230" r="11" fill="#555"/><circle cx="335" cy="230" r="11" fill="#555"/></g>
    <g fill="#444" stroke="none" font-size="16" text-anchor="middle"><text x="110" y="155">2018</text><text x="260" y="155">2020</text><text x="410" y="155">2022</text></g>
    <g fill="var(--green)" stroke="none" font-size="16" text-anchor="middle"><text x="185" y="199">2019</text><text x="335" y="199">2021</text></g>
  </svg>
  <div class="abs" style="left:158px;top:58px;width:55px;text-align:center"><svg width="12" height="14" viewBox="0 0 12 14" fill="var(--green)"><circle cx="8" cy="2" r="1.5"/><path d="M2 14l2-5 2 1 1-4 3 2-1 1-2-1-1 4-2-1-1 3z"/></svg><div style="font-size:4.5px;font-weight:700;color:var(--green)">LOREM IPSUM</div><div class="fine" style="font-size:4px">Lorem ipsum dolor sit amet, consectetur adipiscing elit, Duis elit sapien, convallis vel</div></div>
  <div class="abs" style="left:308px;top:58px;width:55px;text-align:center"><svg width="14" height="14" viewBox="0 0 14 14" fill="var(--green)"><path d="M13 1L6 5 3 5 1 8l3 0 2 2 0 3 3-2 0-3z"/></svg><div style="font-size:4.5px;font-weight:700;color:var(--green)">LOREM IPSUM</div><div class="fine" style="font-size:4px">Lorem ipsum dolor sit amet, consectetur adipiscing elit, Duis elit sapien, convallis vel enim sit amet,</div></div>
  <div class="abs" style="left:83px;top:172px;width:55px;text-align:center"><svg width="12" height="12" viewBox="0 0 12 12" fill="var(--green)"><circle cx="6" cy="3" r="3"/><path d="M0 12a6 6 0 0 1 12 0z"/></svg><div style="font-size:4.5px;font-weight:700;color:var(--green)">LOREM IPSUM</div><div class="fine" style="font-size:4px">Lorem ipsum dolor sit amet, consectetur adipiscing elit, Duis elit sapien,</div></div>
  <div class="abs" style="left:233px;top:172px;width:55px;text-align:center"><svg width="10" height="12" viewBox="0 0 10 12" fill="var(--green)"><path d="M5 0a4 4 0 0 0-2 7.5V10h4V7.5A4 4 0 0 0 5 0zM3 11h4v1H3z"/></svg><div style="font-size:4.5px;font-weight:700;color:var(--green)">LOREM IPSUM</div><div class="fine" style="font-size:4px">Lorem ipsum dolor sit amet, consectetur adipiscing elit. Duis elit sapien, convallis vel</div></div>
  <div class="abs" style="left:383px;top:172px;width:55px;text-align:center"><svg width="14" height="12" viewBox="0 0 14 12" fill="var(--green)"><text x="5" y="5" font-size="6" font-family="Montserrat, sans-serif">$</text><path d="M0 9h4l3 1h4l3-2v2l-3 2H5L0 11z"/></svg><div style="font-size:4.5px;font-weight:700;color:var(--green)">LOREM IPSUM</div><div class="fine" style="font-size:4px">Lorem ipsum dolor sit amet, consectetur adipiscing elit. Duis elit sapien, convallis</div></div>
  <div class="footer">www.r9builders.com<span class="line"></span>13</div>
</section>

<!-- 14 Icon grid -->
<section class="slide c2 r5">
  <div class="brand-tag"><i></i>R9 BUILDERS</div>
  <div class="title">Text Added Hare</div>
  <div class="rule"><b></b><i></i><i></i></div>
  <div class="icon-sq" style="left:94px;top:66px;width:42px;height:42px;background:var(--green)"><svg width="22" height="18" viewBox="0 0 22 18" fill="none" stroke="#fff" stroke-width="1.2"><circle cx="6" cy="5" r="2.5"/><circle cx="16" cy="5" r="2.5"/><path d="M1 13a5 5 0 0 1 10 0M11 13a5 5 0 0 1 10 0"/></svg></div>
  <div class="icon-sq" style="left:247px;top:66px;width:42px;height:42px;background:var(--grey-mid)"><svg width="20" height="20" viewBox="0 0 20 20" fill="none" stroke="#fff" stroke-width="1.2"><circle cx="7" cy="7" r="4"/><circle cx="14" cy="6" r="3"/><circle cx="11" cy="14" r="4"/></svg></div>
  <div class="icon-sq" style="left:401px;top:66px;width:42px;height:42px;background:var(--green)"><svg width="20" height="20" viewBox="0 0 20 20" fill="none" stroke="#fff" stroke-width="1.2"><path d="M3 18V13h3v5M9 18V10h3v8M15 18V7h3v11M3 9l5-4 3 2 6-5M14 2h3v3"/></svg></div>
  <div class="icon-sq" style="left:94px;top:174px;width:42px;height:42px;background:var(--grey-mid)"><svg width="20" height="20" viewBox="0 0 20 20" fill="none" stroke="#fff" stroke-width="1.2"><path d="M3 2v16h15M6 6l4 7 3-2 4 5"/></svg></div>
  <div class="icon-sq" style="left:247px;top:174px;width:42px;height:42px;background:var(--green)"><svg width="18" height="20" viewBox="0 0 18 20" fill="none" stroke="#fff" stroke-width="1.2"><path d="M6 2h6l-2 4a7 7 0 1 1-2 0z"/><text x="6.5" y="16" font-size="7" fill="#fff" stroke="none" font-family="Montserrat, sans-serif">$</text></svg></div>
  <div class="icon-sq" style="left:401px;top:174px;width:42px;height:42px;background:var(--grey-mid)"><svg width="20" height="20" viewBox="0 0 20 20" fill="none" stroke="#fff" stroke-width="1.2"><circle cx="10" cy="8" r="6"/><path d="M7 13l-2 6 5-2 5 2-2-6"/><path d="M10 5l1 2h2l-1.5 1.5.5 2-2-1-2 1 .5-2L7 7h2z"/></svg></div>
  <div class="abs" style="left:65px;top:114px;width:100px;text-align:center"><div style="font-size:7px;font-weight:500">Lorem Ipsum</div><div class="fine" style="font-size:4.3px">Lorem ipsum dolor sit amet, consectetuer adipiscing elit, sed diam nonummy nibh euismod tincidunt ut laoreet</div></div>
  <div class="abs" style="left:218px;top:114px;width:100px;text-align:center"><div class="green" style="font-size:7px;font-weight:500">Lorem ipsum</div><div class="fine" style="font-size:4.3px">Lorem ipsum dolor sit amet, consectetuer adipiscing elit, sed diam nonummy nibh euismod tincidunt ut laoreet</div></div>
  <div class="abs" style="left:372px;top:114px;width:100px;text-align:center"><div style="font-size:7px;font-weight:500">Lorem Ipsum</div><div class="fine" style="font-size:4.3px">Lorem ipsum dolor sit amet, consectetuer adipiscing elit, sed diam nonummy nibh euismod tincidunt ut laoreet</div></div>
  <div class="abs" style="left:65px;top:222px;width:100px;text-align:center"><div class="green" style="font-size:7px;font-weight:500">Lorem ipsum</div><div class="fine" style="font-size:4.3px">Lorem ipsum dolor sit amet, consectetuer adipiscing elit, sed diam nonummy nibh euismod tincidunt ut laoreet</div></div>
  <div class="abs" style="left:218px;top:222px;width:100px;text-align:center"><div style="font-size:7px;font-weight:500">Lorem ipsum</div><div class="fine" style="font-size:4.3px">Lorem ipsum dolor sit amet, consectetuer adipiscing elit, sed diam nonummy nibh euismod tincidunt ut laoreet</div></div>
  <div class="abs" style="left:372px;top:222px;width:100px;text-align:center"><div class="green" style="font-size:7px;font-weight:500">Lorem ipsum</div><div class="fine" style="font-size:4.3px">Lorem ipsum dolor sit amet, consectetuer adipiscing elit, sed diam nonummy nibh euismod tincidunt ut laoreet</div></div>
  <div class="footer">www.r9builders.com<span class="line"></span>14</div>
</section>

<!-- 15 Stacked bars -->
<section class="slide c3 r5">
  <div class="brand-tag"><i></i>R9 BUILDERS</div>
  <div class="title">Text Added Hare</div>
  <div class="rule"><b></b><i></i><i></i></div>
  <svg class="abs" style="left:0;top:0" width="537" height="302" viewBox="0 0 537 302" font-family="Montserrat, sans-serif" font-size="7" fill="#555">
    <line x1="103" y1="60" x2="103" y2="192" stroke="#777" stroke-width=".8"/>
    <circle cx="103" cy="60" r="2" fill="#777"/>
    <circle cx="62" cy="90" r="3.5" fill="var(--green)"/><text x="71" y="93" font-size="8">2019</text>
    <text x="57" y="133" font-size="9" fill="var(--green)">⚓</text><text x="71" y="133" font-size="8">2020</text>
    <circle cx="62" cy="171" r="3.5" fill="var(--green)"/><text x="71" y="174" font-size="8">2021</text>
    <g fill="#fff" text-anchor="middle">
      <rect x="103" y="76" width="51" height="28" fill="var(--green)"/><text x="128" y="93">20%</text>
      <rect x="154" y="76" width="73" height="28" fill="var(--grey-mid)"/><text x="190" y="93">40%</text>
      <rect x="227" y="76" width="50" height="28" fill="var(--green)"/><text x="252" y="93">10%</text>
      <rect x="277" y="76" width="177" height="28" fill="var(--grey-mid)"/><text x="365" y="93">90%</text>
      <rect x="103" y="116" width="124" height="28" fill="var(--grey-mid)"/><text x="165" y="133">50%</text>
      <rect x="227" y="116" width="88" height="28" fill="var(--green)"/><text x="271" y="133">30%</text>
      <rect x="315" y="116" width="72" height="28" fill="var(--grey-mid)"/><text x="351" y="133">20%</text>
      <rect x="387" y="116" width="67" height="28" fill="var(--green)"/><text x="420" y="133">20%</text>
      <rect x="103" y="157" width="70" height="28" fill="var(--green)"/><text x="138" y="174">30%</text>
      <rect x="173" y="157" width="107" height="28" fill="var(--grey-mid)"/><text x="226" y="174">60%</text>
      <rect x="280" y="157" width="33" height="28" fill="var(--green)"/><text x="296" y="174">10%</text>
      <rect x="313" y="157" width="141" height="28" fill="var(--grey-mid)"/><text x="383" y="174">70%</text>
    </g>
    <g text-anchor="middle" font-size="6.5"><text x="103" y="213">0%</text><text x="138" y="213">10%</text><text x="173" y="213">20%</text><text x="208" y="213">30%</text><text x="243" y="213">40%</text><text x="279" y="213">50%</text><text x="314" y="213">60%</text><text x="349" y="213">70%</text><text x="384" y="213">80%</text><text x="419" y="213">90%</text><text x="454" y="213">100%</text></g>
  </svg>
  <div class="abs" style="left:95px;top:225px;width:80px"><div class="green" style="font-size:6.5px;font-weight:500">Lorem Ipsum</div><div class="fine" style="font-size:3.8px">Lorem ipsum dolor sit amet, consectetuer adipiscing elit, sed diam nonummy nibh euismod tincid</div></div>
  <div class="abs" style="left:190px;top:225px;width:80px"><div class="green" style="font-size:6.5px;font-weight:500">Lorem Ipsum</div><div class="fine" style="font-size:3.8px">Lorem ipsum dolor sit amet, consectetuer adipiscing elit, sed diam nonummy nibh euismod tincid</div></div>
  <div class="abs" style="left:290px;top:225px;width:80px"><div class="green" style="font-size:6.5px;font-weight:500">Lorem Ipsum</div><div class="fine" style="font-size:3.8px">Lorem ipsum dolor sit amet, consectetuer adipiscing elit, sed diam nonummy nibh euismod tincid</div></div>
  <div class="abs" style="left:391px;top:225px;width:80px"><div class="green" style="font-size:6.5px;font-weight:500">Lorem Ipsum</div><div class="fine" style="font-size:3.8px">Lorem ipsum dolor sit amet, consectetuer adipiscing elit, sed diam nonummy nibh euismod tincid</div></div>
  <div class="footer">www.r9builders.com<span class="line"></span>15</div>
</section>

<!-- 16 Text columns -->
<section class="slide c1 r6">
  <div class="brand-tag"><i></i>R9 BUILDERS</div>
  <div class="title">Text Added Hare</div>
  <div class="rule"><b></b><i></i><i></i></div>
  <div class="abs" style="left:32px;top:68px;width:146px"><div class="green" style="font-size:7px;font-weight:500">1. Text Added Here</div><div class="fine" style="font-size:4.3px;text-align:justify">Lorem ipsum dolor sit amet, cons ectetuer adipiscing elit, sed diam nonummy nibh euismod tincidunt ut laoreet dolore magna aliquam erat volutpat. Ut wisi enim ad minim veniam, quis nostrud exerci tation ullamcorper suscipit lobortis nisl ut aliquip ex ea commodo consequat.<br><br>Lorem ipsum dolor sit amet, consectetuer adipiscing elit, sed diam nonummy nibh euismod tincidunt ut laoreet dolore magna aliquam erat volutpat.</div></div>
  <div class="abs" style="left:199px;top:68px;width:146px"><div style="font-size:7px;font-weight:500">1. Text Added Here</div><div class="fine" style="font-size:4.3px;text-align:justify">Lorem ipsum dolor sit amet, cons ectetuer adipiscing elit, sed diam nonummy nibh euismod tincidunt ut laoreet dolore magna aliquam erat volutpat. Ut wisi enim ad suscipit lobortis nisl ut aliquip ex ea commodo consequat.<br><br>Lorem ipsum dolor sit amet, consectetuer adipiscing elit, Ut wisi enim ad minim veniam, quis nostrud exerci tation ullamcorper suscipit lobortis nisl ut aliquip ex ea commodo consequat.</div></div>
  <div class="abs" style="left:360px;top:68px;width:146px"><div class="green" style="font-size:7px;font-weight:500">1. Text Added Here</div><div class="fine" style="font-size:4.3px;text-align:justify">Lorem ipsum dolor sit amet, cons ectetuer adipiscing elit, sed diam nonummy nibh euismod tincidunt ut laoreet dolore magna aliquam erat volutpat.<br><br>Lorem ipsum dolor sit amet, consectetuer adipiscing elit, sed diam nonummy nibh euismod tincidunt ut laoreet dolore magna aliquam erat volutpat. Ut wisi enim ullamcorper suscipit lobortis nisl ut aliquip ex ea commodo consequat.</div></div>
  <div class="abs" style="left:32px;top:165px;width:146px"><div style="font-size:7px;font-weight:500">1. Text Added Here</div><div class="fine" style="font-size:4.3px;text-align:justify">Lorem ipsum dolor sit amet, cons ectetuer adipiscing elit, sed diam nonummy nibh euismod tincidunt ut laoreet dolore magna aliquam erat volutpat. Ut wisi enim ad minim veniam, ea commodo consequat.<br><br>Lorem ipsum dolor sit amet, consectetuer adipiscing elit, sed diam nonummy nibh euismod enim ad minim veniam, quis nostrud exerci tation ullamcorper suscipit lobortis nisl ut aliquip ex ea</div></div>
  <div class="abs" style="left:199px;top:165px;width:146px"><div class="green" style="font-size:7px;font-weight:500">1. Text Added Here</div><div class="fine" style="font-size:4.3px;text-align:justify">Lorem ipsum dolor sit amet, cons ectetuer adipiscing elit, sed diam nonummy nibh euismod tincidunt ut laoreet dolore magna aliquam erat volutpat. Ut wisi ea commodo consequat.<br><br>Lorem ipsum dolor sit amet, consectetuer adipiscing elit, sed diam nonummy nibh euismod tincidunt ut laoreet tation ullamcorper suscipit lobortis nisl ut aliquip ex ea commodo consequat.</div></div>
  <div class="abs" style="left:360px;top:165px;width:146px"><div style="font-size:7px;font-weight:500">1. Text Added Here</div><div class="fine" style="font-size:4.3px;text-align:justify">Lorem ipsum dolor sit amet, cons ectetuer adipiscing elit, sed diam nonummy nibh euismod tincidunt ut laoreet dolore magna ea commodo consequat.<br><br>Lorem ipsum dolor sit amet, consectetuer adipiscing elit, sed diam nonummy nibh euismod tincidunt ut laoreet dolore magna aliquam erat volutpat. Ut wisi enim suscipit lobortis nisl ut aliquip ex ea commodo consequat.</div></div>
  <div class="footer">www.r9builders.com<span class="line"></span>16</div>
</section>

<!-- 17 Team -->
<section class="slide c2 r6">
  <div class="brand-tag"><i></i>R9 BUILDERS</div>
  <div class="title">Text Added Hare</div>
  <div class="rule"><b></b><i></i><i></i></div>
  <div class="abs" style="left:49px;top:95px;width:79px;height:30px;background:var(--green)"></div>
  <div class="abs" style="left:167px;top:95px;width:79px;height:30px;background:var(--grey-mid)"></div>
  <div class="abs" style="left:287px;top:95px;width:79px;height:30px;background:var(--green)"></div>
  <div class="abs" style="left:409px;top:95px;width:79px;height:30px;background:var(--grey-mid)"></div>
  <div class="abs" role="img" aria-label="Team member portrait" style="left:67px;top:105px;width:42px;height:42px;border-radius:50%;border:3px solid #fff;background:linear-gradient(160deg,#c9c9c9,#8d8d8d)"></div>
  <div class="abs" role="img" aria-label="Team member portrait" style="left:185px;top:105px;width:42px;height:42px;border-radius:50%;border:3px solid #fff;background:linear-gradient(160deg,#c9c9c9,#8d8d8d)"></div>
  <div class="abs" role="img" aria-label="Team member portrait" style="left:305px;top:105px;width:42px;height:42px;border-radius:50%;border:3px solid #fff;background:linear-gradient(160deg,#c9c9c9,#8d8d8d)"></div>
  <div class="abs" role="img" aria-label="Team member portrait" style="left:427px;top:105px;width:42px;height:42px;border-radius:50%;border:3px solid #fff;background:linear-gradient(160deg,#c9c9c9,#8d8d8d)"></div>
  <div class="abs" style="left:43px;top:157px;width:91px;text-align:center"><div style="font-size:7px;font-weight:600">DAVID REYES</div><div class="fine" style="font-size:4px;margin-top:2px">ipsum dolor sit amet, cons ectetuer adipiscing elit, sed diam nonummy nibh euismod tincidunt<br><br>ut laoreet dolore magna aliquam erat volutpat. Ut wisi enim ad minim veniam, quis nostrud</div></div>
  <div class="abs" style="left:161px;top:157px;width:91px;text-align:center"><div style="font-size:7px;font-weight:600">ANNA COLE</div><div class="fine" style="font-size:4px;margin-top:2px">ipsum dolor sit amet, cons ectetuer adipiscing elit, sed diam nonummy nibh euismod tincidunt ut laoreet dolore magna<br><br>aliquam erat volutpat. Ut wisi enim ad minim veniam, quis nostrud</div></div>
  <div class="abs" style="left:281px;top:157px;width:91px;text-align:center"><div style="font-size:7px;font-weight:600">DAVID REYES</div><div class="fine" style="font-size:4px;margin-top:2px">ipsum dolor sit amet, cons ectetuer adipiscing elit, sed diam nonummy nibh euismod tincidunt ut laoreet dolore magna aliquam erat volutpat.<br><br>Ut wisi enim ad minim veniam, quis nostrud</div></div>
  <div class="abs" style="left:403px;top:157px;width:91px;text-align:center"><div style="font-size:7px;font-weight:600">ANNA COLE</div><div class="fine" style="font-size:4px;margin-top:2px">ipsum dolor sit amet, cons ectetuer adipiscing elit, sed diam nonummy nibh euismod tincidunt ut laoreet dolore magna<br><br>aliquam erat volutpat. Ut wisi enim ad minim veniam, quis nostrud</div></div>
  <div class="footer">www.r9builders.com<span class="line"></span>17</div>
</section>

<!-- 18 Contact -->
<section class="slide c3 r6" style="background:#555">
  <div class="photo" style="inset:0;background:linear-gradient(160deg,#6e6e6e,#444)" role="img" aria-label="Interior remodeling site, darkened greyscale"></div>
  <div class="abs white" style="left:30px;top:130px;width:210px;text-align:center">
    <div style="display:inline-flex;align-items:center;gap:6px;font-size:12px;font-weight:700;letter-spacing:2px"><i style="display:block;width:12px;height:12px;background:var(--green)"></i>R9 BUILDERS CORP.</div>
  </div>
  <div class="abs" style="left:254px;top:97px;width:283px;height:100px;background:var(--green)"></div>
  <div class="abs" style="left:270px;top:108px;font-size:7.5px;line-height:1.45;color:#2f2f2f">
    <div style="font-weight:700">R9 Builders Corp.</div>
    <div style="font-style:italic">2207 Larkfield Ave. Suite 310</div>
    <div style="font-style:italic">Fairview, CA 90210</div>
    <div style="font-style:italic">555-014-2290</div>
    <div>LICENSE NO. 0000000</div>
  </div>
</section>

</body>
</html>
```